Vela Errands Web Design Project

Homepage components
o Logo
o Rotating header
o Main menu
o Animation video
o Banners
o Members login
o Latest news

The design’s preferred colors are black (background), silver (main tabs) and white (text)

Site map:
• Home
• News
• About us
o Welcome Note
o Company Profile
• Member Log in
o Registered homepage
? Request a service (form)
? Services directory
? Update profile
? Services history
• Member registration
o Registration form
• Partners
Footer Menu
• Contact us
• Terms & Conditions
• Privacy policy
• Social media links
• Sitemap

Brief about the company:
Vela Errands is a Jordanian company dedicated to elevate and redefine the level of service in the country. We are set out to give premium services at affordable prices. In this fast paced environment that we live in, we barely have the luxury of free time anymore and we, at Vela Errands will be giving you that extra hour or two per day to spend as your heart desires!
By becoming a member you will get access to a world of comfort and peace of mind. We have done the homework on your behalf and have established the network of connections that will enable you to live a headache free life.
We will be providing our members with support and assistance in their day to day lives in the fields that consumes and wastes time the most. We are value driven and below is our “ever-growing” list of services that we will provide at excellent prices:
• Maintenance (carpentry, plumbing, electrical, painting, decorating, gardening… etc)
• Cleaning (pre and post tenancy, periodical deep cleaning, packing and moving services, laundry… etc)
• Personalized delivery services (grocery, important documents, office related supplies, posting cheques, food, paying bills… etc)
• Passport, driving license and ID reissuance
• Travel arrangements (flights, hotels, airport transfers… etc)
• Premium car rental services
• Restaurant reservations
• IT assistance
• Event planning and all related services
• Catering arrangements

Aside from all the services we have on offer we have collaborated with a number of places (that we like to call partners) in town where Vela Errands members are entitled to benefits and privileges that will most certainly add value to their membership. Alongside our partners we have come up with the best formula that will please our members. Below are some of our current partners:

Requirements
Must have
• Homepage components
o Logo
o Rotating header
o Main menu
o Animation video
o Banners
o Members login
o Latest news

```html
<!DOCTYPE html>
<html lang="en">
<head>
<meta charset="utf-8">
<title>Vela Errands</title>
<link rel="stylesheet" href="https://fonts.googleapis.com/css2?family=Noto+Serif:wght@400&family=PT+Sans:wght@400;700&display=swap">
<style>
  :root {
    --page-bg: #000;
    --panel-bg: #f1f1f3;
    --footer-bg: #4b4b4b;
    --silver-top: #a9a9a9;
    --silver-bottom: #7d7d7d;
    --heading: #111;
    --body-text: #555;
    --rule: #cfcfd2;
    --white: #fff;
    --input-border: #d4d4d8;
    --video-fill: #c9c9c9;
  }
  * { box-sizing: border-box; margin: 0; padding: 0; }
  html, body { width: 1200px; height: 1001px; overflow: hidden; }
  body {
    position: relative;
    background: radial-gradient(ellipse 360px 140px at 250px 40px, #3a3a3a 0%, #0d0d0d 70%, var(--page-bg) 100%);
    font-family: "Noto Serif", Georgia, serif;
    color: var(--body-text);
  }
  .abs { position: absolute; }

  /* Header */
  .brand {
    left: 178px; top: 34px;
    font-family: "Noto Serif", Georgia, serif;
    font-size: 34px; color: var(--white); letter-spacing: .5px;
  }
  .brand-tagline {
    left: 205px; top: 76px; font-family: "PT Sans", sans-serif;
    font-size: 11px; color: #ddd;
  }
  .register-tab {
    left: 937px; top: 0; width: 117px; height: 33px;
    border: 3px solid #8a8a8a; border-top: none; border-radius: 0 0 9px 9px;
    background: linear-gradient(#3b3b3b, #111);
    color: var(--white); font-family: "PT Sans", sans-serif; font-size: 14px; font-weight: 700;
    text-align: center; line-height: 30px; text-decoration: none;
  }
  .main-nav {
    left: 566px; top: 49px; width: 484px; height: 30px; display: flex;
    border-radius: 3px; overflow: hidden;
    background: linear-gradient(var(--silver-top), var(--silver-bottom));
  }
  .main-nav a {
    flex: 1; text-align: center; line-height: 30px;
    color: var(--white); font-family: "PT Sans", sans-serif; font-size: 12px; font-weight: 700;
    text-decoration: none; border-left: 1px solid #6f6f6f;
  }
  .main-nav a:first-child { border-left: none; }

  /* Rotating header */
  .hero {
    left: 142px; top: 112px; width: 915px; height: 375px;
    border: 1px solid #999; border-radius: 6px;
    background: linear-gradient(100deg, #2e2e2e 0%, #6e6e6e 35%, #bdbdbd 60%, #e6e6e6 80%, #9a9a9a 100%);
  }
  .hero-arrow {
    top: 169px; width: 57px; height: 35px;
    background: rgba(150,150,150,.7);
  }
  .hero-arrow.prev { left: 0; border-radius: 0 4px 4px 0; }
  .hero-arrow.next { right: 0; border-radius: 4px 0 0 4px; }
  .hero-arrow svg { position: absolute; left: 22px; top: 10px; }

  /* Content panel */
  .panel { left: 143px; top: 503px; width: 914px; height: 436px; background: var(--panel-bg); }
  .section-title { font-size: 23px; color: var(--heading); font-weight: 400; line-height: 1; }
  .rule { height: 1px; background: var(--rule); }
  .welcome-text {
    left: 187px; top: 566px; width: 504px;
    font-size: 11.3px; line-height: 20.3px; text-align: justify;
  }
  .welcome-text p + p { margin-top: 20.3px; }

  .video {
    left: 725px; top: 548px; width: 300px; height: 184px;
    border: 6px solid #000; background: linear-gradient(90deg, #d2d2d2, var(--video-fill));
  }
  .video .play { position: absolute; left: 127px; top: 76px; }

  .field {
    width: 200px; height: 31px; border: 1px solid var(--input-border); border-radius: 7px;
    background: var(--white); font-family: "Noto Serif", serif; font-size: 11.5px; color: #666;
    padding-left: 13px;
  }
  .login-btn {
    left: 295px; top: 893px; width: 91px; height: 30px;
    border: 1px solid #9c9c9c; border-radius: 2px;
    background: linear-gradient(#f4f4f4, #c9c9c9);
    font-family: "Noto Serif", serif; font-size: 14px; color: #222;
  }

  .bullets { list-style: none; font-size: 11.3px; color: #222; }
  .bullets li { position: relative; padding-left: 20px; height: 20.3px; line-height: 20.3px; }
  .bullets li::before {
    content: ""; position: absolute; left: 1px; top: 7px;
    border-left: 4px solid #111; border-top: 3px solid transparent; border-bottom: 3px solid transparent;
  }
  .news { list-style: none; font-size: 11.3px; color: #555; width: 290px; }
  .news li { position: relative; padding-left: 23px; line-height: 16.5px; }
  .news li::before {
    content: ""; position: absolute; left: 4px; top: 5px;
    border-left: 4px solid #111; border-top: 3px solid transparent; border-bottom: 3px solid transparent;
  }

  /* Footer */
  .site-footer { left: 0; top: 939px; width: 1200px; height: 62px; background: var(--footer-bg); }
  .footer-links {
    left: 0; width: 1234px; top: 951px; text-align: center;
    font-family: "PT Sans", sans-serif; font-size: 12px; color: #eee;
  }
  .footer-links a { color: #eee; text-decoration: none; }
  .footer-links .sep { margin: 0 7px; }
  .copyright {
    left: 0; width: 1234px; top: 971px; text-align: center;
    font-family: "PT Sans", sans-serif; font-size: 12px; color: #eee;
  }
  .social { top: 958px; width: 28px; height: 28px; border-radius: 3px; }
  .social.one { left: 957px; background: #4a67a8; }
  .social.two { left: 994px; background: #5cb6e4; }
</style>
</head>
<body>
  <header>
    <div class="abs brand">Vela Errands</div>
    <div class="abs brand-tagline">we make life easier</div>
    <a class="abs register-tab" href="#">Register here</a>
    <nav class="abs main-nav">
      <a href="#">Home</a><a href="#">News</a><a href="#">About Us</a><a href="#">Login</a><a href="#">Partners</a>
    </nav>
  </header>

  <div class="abs hero" role="img" aria-label="Black and white photo of a handshake between a customer and a smiling couple">
    <div class="abs hero-arrow prev"><svg width="12" height="15" viewBox="0 0 12 15"><path d="M9 1.5 3 7.5l6 6" fill="none" stroke="#111" stroke-width="3"/></svg></div>
    <div class="abs hero-arrow next"><svg width="12" height="15" viewBox="0 0 12 15"><path d="M3 1.5 9 7.5l-6 6" fill="none" stroke="#111" stroke-width="3"/></svg></div>
  </div>

  <main>
    <div class="abs panel"></div>

    <h2 class="abs section-title" style="left:157px;top:518px;">Welcome to our site</h2>
    <div class="abs rule" style="left:178px;top:551px;width:512px;"></div>
    <div class="abs welcome-text">
      <p>Vela Errands is a Jordanian company dedicated to elevate and redefine the level of service in the country. We are set out to give premium services at affordable prices. In this fast paced environment that we live in, we barely have the luxury of free time anymore and we, at Vela Errands will be giving you that extra hour or two per day to spend as your heart desires!</p>
      <p>premium services at affordable prices. In this fast paced environment that we live in, we barely have the luxury of free time anymore and we, at Vela Errands will be giving you that extra hour or two per day to spend as your heart desires!</p>
    </div>

    <h2 class="abs section-title" style="left:706px;top:518px;">Our Video</h2>
    <div class="abs video" role="img" aria-label="Video still of a smiling woman seated at a laptop">
      <svg class="play" width="30" height="30" viewBox="0 0 30 30"><circle cx="15" cy="15" r="15" fill="#111"/><path d="M12 10v10l8-5z" fill="#ddd"/></svg>
    </div>

    <h2 class="abs section-title" style="left:178px;top:762px;">login</h2>
    <div class="abs rule" style="left:178px;top:792px;width:218px;"></div>
    <input class="abs field" style="left:186px;top:805px;" type="text" placeholder="Username">
    <input class="abs field" style="left:186px;top:843px;" type="password" placeholder="Password">
    <button class="abs login-btn" type="button">Login</button>

    <h2 class="abs section-title" style="left:411px;top:762px;">Our Services</h2>
    <div class="abs rule" style="left:411px;top:792px;width:255px;"></div>
    <ul class="abs bullets" style="left:411px;top:799px;">
      <li>Lorem Ipsum</li><li>Harbour College</li><li>Renaissance</li><li>Morbi ultrices sollicitudin</li><li>Nullam convallis</li>
    </ul>
    <ul class="abs bullets" style="left:579px;top:799px;">
      <li>Lorem Ipsum</li><li>Harbour College</li><li>Renaissance</li><li>Morbi ultrices</li><li>Nullam convallis</li>
    </ul>

    <h2 class="abs section-title" style="left:724px;top:761px;">Latest News</h2>
    <div class="abs rule" style="left:724px;top:789px;width:304px;"></div>
    <ul class="abs news" style="left:724px;top:801px;">
      <li>Maintenance (carpentry, plumbing, electrical, painting, decorating, gardening… etc)</li>
      <li style="margin-top:13px;">Cleaning (pre and post tenancy, periodical deep cleaning, packing and moving services, laundry…</li>
      <li style="margin-top:17px;">Passport, driving license and ID reissuance</li>
    </ul>
  </main>

  <footer>
    <div class="abs site-footer"></div>
    <div class="abs footer-links"><a href="#">Terms &amp; conditions</a><span class="sep">|</span><a href="#">Privacy Policy</a><span class="sep">|</span><a href="#">Site map</a></div>
    <div class="abs copyright">Copyrights @ 2012 All Rights Reserved</div>
    <div class="abs social one" aria-label="Social link"></div>
    <div class="abs social two" aria-label="Social link"></div>
  </footer>
</body>
</html>
```